Quillmark Select

Letter Head, Envelope, Business Cards, Social Media Banner (FB/Twitter), Social Media Icon, Social Media Announcement Template...

We are a Softball Team/Organization

Target Market(s)

High School Student-Athletes (softball players) and their parents

Font styles to use
Serif

Requirements
Must have
• Logo & Colors
Must POP and say WOW
Common theme amongst all designs

```html
<!DOCTYPE html>
<html lang="en">
<head>
<meta charset="utf-8">
<title>Quillmark Select — Business Card</title>
<link href="https://fonts.googleapis.com/css2?family=Montserrat:wght@400;500;600&display=swap" rel="stylesheet">
<style>
  :root {
    --backdrop: #8a8a8a;
    --navy: #1f3764;
    --navy-deep: #0d1a35;
    --royal: #3058c0;
    --paper: #ffffff;
    --ink: #4a4a4a;
  }
  * { margin: 0; padding: 0; box-sizing: border-box; }
  html, body {
    width: 1200px; height: 1200px; overflow: hidden;
    background: var(--backdrop);
    font-family: "Montserrat", sans-serif;
  }
  .stage { position: relative; width: 1200px; height: 1200px; }
  .card {
    position: absolute; left: 262px; width: 686px; height: 392px;
    overflow: hidden;
  }
  .card--front { top: 165px; background: var(--paper); }
  .card--back { top: 653px; background: var(--navy); }

  .name-band {
    position: absolute; left: 0; top: 40px; width: 390px; height: 114px;
    background: var(--navy); color: var(--paper);
    padding: 34px 0 0 43px;
  }
  .name-band__name { font-size: 23px; font-weight: 500; letter-spacing: 0.3px; line-height: 1.1; white-space: nowrap; }
  .name-band__title { font-size: 16px; font-weight: 500; margin-top: 3px; }

  .brand {
    position: absolute; right: 43px; top: 84px;
    display: flex; align-items: center; gap: 9px;
    color: var(--navy); font-size: 17px; font-weight: 600; letter-spacing: 1.2px;
    white-space: nowrap;
  }
  .brand__mark { width: 13px; height: 13px; background: var(--navy); flex: none; }

  .contact {
    position: absolute; left: 43px; top: 296px;
    list-style: none; color: var(--ink); font-size: 15.5px; line-height: 19.5px;
  }
  .contact li { display: flex; align-items: center; gap: 8px; white-space: nowrap; }
  .contact svg { width: 12px; height: 12px; fill: var(--navy); flex: none; }

  .address {
    position: absolute; right: 43px; top: 296px; text-align: right;
    color: var(--ink); font-size: 15.5px; line-height: 19.5px; font-style: normal;
    white-space: nowrap;
  }
  .address__web { color: var(--navy); font-weight: 600; margin-top: 3px; display: block; }

  .back-pattern {
    position: absolute; inset: 0;
    background: linear-gradient(100deg, var(--royal) 0%, var(--navy) 45%, var(--navy-deep) 100%);
    opacity: 0.55;
  }
  .back-brand {
    position: absolute; left: 470px; top: 258px;
    display: flex; align-items: center; gap: 8px;
    color: var(--paper); font-size: 15px; font-weight: 600; letter-spacing: 1.2px;
    white-space: nowrap;
  }
  .back-brand__mark { width: 12px; height: 12px; background: var(--paper); flex: none; }
</style>
</head>
<body>
<main class="stage">
  <section class="card card--front">
    <div class="name-band">
      <p class="name-band__name">DANIEL HARPER</p>
      <p class="name-band__title">President</p>
    </div>
    <div class="brand"><span class="brand__mark"></span>QUILLMARK SELECT</div>

    <ul class="contact">
      <li><svg viewBox="0 0 24 24"><path d="M6.6 10.8a15 15 0 0 0 6.6 6.6l2.2-2.2c.3-.3.7-.4 1-.2 1.1.4 2.3.6 3.6.6.6 0 1 .4 1 1V20c0 .6-.4 1-1 1A17 17 0 0 1 3 4c0-.6.4-1 1-1h3.5c.6 0 1 .4 1 1 0 1.3.2 2.5.6 3.6.1.3 0 .7-.2 1z"/></svg>555-214-0386</li>
      <li><svg viewBox="0 0 24 24"><path d="M7 1h10a2 2 0 0 1 2 2v18a2 2 0 0 1-2 2H7a2 2 0 0 1-2-2V3a2 2 0 0 1 2-2zm0 3v14h10V4z"/></svg>555-418-2730</li>
      <li><svg viewBox="0 0 24 24"><path d="M2 5h20v14H2zm2 2v.5l8 5 8-5V7l-8 5z"/></svg>info@quillmarkselect.com</li>
    </ul>

    <address class="address">
      1420 Birchwood Avenue<br>
      Maplewood, Oregon 97410
      <span class="address__web">www.quillmarkselect.com</span>
    </address>
  </section>

  <section class="card card--back">
    <div class="back-pattern" role="img" aria-label="Embossed repeating star pattern fading from bright blue to deep navy"></div>
    <div class="back-brand"><span class="back-brand__mark"></span>QUILLMARK SELECT</div>
  </section>
</main>
</body>
</html>
```